New Postcard for Sales and Marketing Push Summer/Fall of 2026

We need a postcard design for security guard services based in NJ. We provide Armed and Unarmed security guards to warehouses, cannabis facilities, gated communites, Construction sites.

I would also like you to mention it is owned and operated by a retired law enforcement officer we customize our services to the clients needs.

Our services include Armed and Unarmed guards, Permanent and Emergency security coverage, Property Checks, Fire Watches, Alarm Response, Mobile patrols, ALPR camera systems and Mobile security cameras.

```html
<!DOCTYPE html>
<html lang="en">
<head>
<meta charset="utf-8">
<title>Vanter Security Postcard</title>
<link href="https://fonts.googleapis.com/css2?family=Archivo+Black&family=Roboto:wght@400;500;700;900&family=Roboto+Condensed:wght@700&display=swap" rel="stylesheet">
<style>
:root{
  --navy:#131b4a;
  --navy-deep:#0f1640;
  --blue:#1b8fd1;
  --blue-dark:#156fae;
  --ink:#1c2555;
  --text:#222;
  --white:#fff;
  --backdrop:#bdb9b8;
  --rule:#d9d9d9;
  --stamp:#e4e4e4;
}
*{box-sizing:border-box;margin:0;padding:0}
html,body{width:907px;height:1200px;overflow:hidden}
body{background:var(--backdrop);font-family:"Roboto",sans-serif;position:relative}
.card{position:absolute;left:49px;width:801px;height:534px;background:var(--white);overflow:hidden}
.card--front{top:47px}
.card--back{top:614px}
.layer{position:absolute;left:0;top:0;width:801px;height:534px}

.brand{position:absolute;display:flex;align-items:center;gap:8px}
.brand__mark{width:34px;height:34px;border-radius:50%;background:var(--blue)}
.brand__name{font-family:"Roboto",sans-serif;font-weight:900;color:var(--ink);line-height:1;letter-spacing:1px}
.brand__sub{position:absolute;font-family:"Roboto Condensed",sans-serif;font-weight:700;color:var(--ink);letter-spacing:2.6px;white-space:nowrap}

.headline{position:absolute;font-family:"Archivo Black",sans-serif;line-height:1;letter-spacing:-1px;transform-origin:left top;
  background:linear-gradient(90deg,var(--blue) 0%,var(--blue-dark) 45%,var(--blue) 100%);
  -webkit-background-clip:text;background-clip:text;color:transparent;white-space:nowrap}
.subhead{position:absolute;font-family:"Roboto Condensed",sans-serif;font-weight:700;white-space:nowrap;line-height:1}
.rule{position:absolute;height:1.5px;background:var(--blue)}
.tagline{position:absolute;font-size:14.5px;letter-spacing:2.2px;color:var(--text);white-space:nowrap}

.owner-banner{position:absolute;left:29px;top:276px;width:393px;height:46px;background:var(--blue);border-radius:0 5px 5px 0;padding-left:55px;color:var(--white)}
.owner-banner__small{font-size:12px;font-weight:500;margin-top:5px;letter-spacing:.3px}
.owner-banner__big{font-family:"Roboto Condensed",sans-serif;font-weight:700;font-size:18.5px;letter-spacing:.4px;line-height:20px;white-space:nowrap}
.owner-banner__badge{position:absolute;left:-4px;top:-3px}

.sectors-title{position:absolute;left:27px;top:341px;font-family:"Roboto Condensed",sans-serif;font-weight:700;font-size:15.5px;color:var(--blue);letter-spacing:.6px}
.sector{position:absolute;top:372px;width:100px;margin-left:-50px;text-align:center;color:var(--ink);font-size:13.5px;line-height:16.5px;font-weight:500}
.sector svg{display:block;margin:0 auto 11px}
.sector-divider{position:absolute;top:360px;width:1px;height:84px;background:#c9cdd8}

.region{position:absolute;left:640px;width:150px;text-align:center;color:var(--white)}
.region__small{font-family:"Roboto Condensed",sans-serif;font-weight:700;font-size:11px;letter-spacing:.4px}
.region__big{font-family:"Roboto Condensed",sans-serif;font-weight:700;font-size:22px;color:var(--blue);letter-spacing:.8px;line-height:24px}

.cta{position:absolute;left:85px;top:462px;color:var(--white);font-family:"Roboto Condensed",sans-serif;font-weight:700;white-space:nowrap}
.cta__top{font-size:17px;letter-spacing:.6px;line-height:20px}
.cta__free{font-size:35px;line-height:34px}
.cta__rest{font-size:17.5px;margin-left:4px}
.cta__icon{position:absolute;left:27px;top:472px}

.contact{position:absolute;color:var(--white);font-size:19px;line-height:22px;white-space:nowrap}
.contact__row{display:flex;align-items:center;gap:9px;height:21px}
.contact__row .hl{color:var(--blue)}

.section-title{position:absolute;left:27px;font-family:"Roboto Condensed",sans-serif;font-weight:700;font-size:16px;color:var(--white);padding-left:10px;border-left:4px solid var(--blue);line-height:16px;letter-spacing:.3px}
.reason{position:absolute;display:flex;align-items:center;gap:10px;color:var(--white);font-size:11.5px;font-weight:500;line-height:14.5px}
.reason-divider{position:absolute;width:1px;height:28px;background:#5a6392}
.service{position:absolute;display:flex;align-items:center;gap:8px;color:var(--white);font-size:11.5px;line-height:13px}

.stamp{position:absolute;left:671px;top:28px;width:103px;height:109px;background:var(--stamp)}
.address-line{position:absolute;height:1px;background:var(--rule)}
</style>
</head>
<body>

<!-- FRONT -->
<section class="card card--front">
  <svg class="layer" viewBox="0 0 801 534" aria-hidden="true">
    <defs>
      <linearGradient id="ctaBlue" x1="0" x2="1"><stop offset="0" stop-color="#1b8fd1"/><stop offset="1" stop-color="#156fae"/></linearGradient>
    </defs>
    <path d="M363,472 H801 V534 H385 Z" fill="#131b4a"/>
    <path d="M0,459 H352 Q362,459 366,468 L385,534 H0 Z" fill="url(#ctaBlue)"/>
  </svg>

  <svg class="layer" viewBox="0 0 801 534">
    <defs>
      <linearGradient id="scene" x1="0" y1="0" x2="0.3" y2="1">
        <stop offset="0" stop-color="#6f87ad"/>
        <stop offset="0.45" stop-color="#2f4a7a"/>
        <stop offset="1" stop-color="#131b4a"/>
      </linearGradient>
    </defs>
    <path d="M455,0 H801 V534 H650 C560,470 480,330 440,130 C432,70 436,20 455,0 Z" fill="#1b8fd1"/>
    <path d="M478,0 H801 V508 C760,528 712,528 682,512 C582,450 502,320 463,140 C453,80 456,25 478,0 Z" fill="#131b4a"/>
    <path d="M498,14 C488,20 484,30 484,50" fill="none" stroke="#1b8fd1" stroke-width="3"/>
    <path role="img" aria-label="Photo of a security officer watching a wall of CCTV monitors in a control room" d="M515,24 H801 V470 C760,490 720,488 695,475 C600,420 525,300 496,150 C488,100 492,50 515,24 Z" fill="url(#scene)"/>
  </svg>

  <div class="brand" style="left:37px;top:30px">
    <span class="brand__mark"></span>
    <span class="brand__name" style="font-size:62px">VANTER</span>
  </div>
  <div class="brand__sub" style="left:92px;top:104px;font-size:16px">SECURITY &amp; INVESTIGATIONS</div>

  <div class="headline" style="left:26px;top:142px;font-size:60px;transform:scaleX(1.27)">PROTECT</div>
  <div class="subhead" style="left:27px;top:200px;font-size:33px;letter-spacing:4.8px;color:var(--ink)">WHAT MATTERS MOST</div>
  <div class="rule" style="left:28px;top:238px;width:393px"></div>
  <div class="tagline" style="left:27px;top:247px">Professional Armed &amp; Unarmed Security Services</div>

  <div class="owner-banner">
    <svg class="owner-banner__badge" width="50" height="52" viewBox="0 0 50 52" aria-hidden="true">
      <path d="M25,2 C34,6 42,7 48,7 C48,30 40,44 25,50 C10,44 2,30 2,7 C8,7 16,6 25,2 Z" fill="#131b4a" stroke="#fff" stroke-width="2"/>
      <path d="M16,26 L22,32 L34,19" fill="none" stroke="#fff" stroke-width="3" stroke-linecap="round" stroke-linejoin="round"/>
    </svg>
    <div class="owner-banner__small">OWNED &amp; OPERATED BY A</div>
    <div class="owner-banner__big">RETIRED LAW ENFORCEMENT OFFICER</div>
  </div>

  <div class="sectors-title">CUSTOMIZED SECURITY SOLUTIONS FOR:</div>

  <div class="sector" style="left:67px">
    <svg width="36" height="34" viewBox="0 0 36 34" fill="none" stroke="#131b4a" stroke-width="2"><path d="M2,12 L18,3 L34,12 V33 H2 Z"/><path d="M8,33 V16 H28 V33"/><path d="M14,33 V26 H22 V33"/></svg>
    Warehouses
  </div>
  <div class="sector-divider" style="left:114px"></div>
  <div class="sector" style="left:163px">
    <svg width="36" height="34" viewBox="0 0 36 34" fill="none" stroke="#131b4a" stroke-width="2"><path d="M18,3 C24,10 24,20 18,26 C12,20 12,10 18,3 Z"/><path d="M18,26 C11,24 5,18 3,12 C10,13 16,19 18,26 Z"/><path d="M18,26 C25,24 31,18 33,12 C26,13 20,19 18,26 Z"/><path d="M18,26 V33"/></svg>
    Cannabis<br>Facilities
  </div>
  <div class="sector-divider" style="left:206px"></div>
  <div class="sector" style="left:259px">
    <svg width="36" height="34" viewBox="0 0 36 34" fill="none" stroke="#131b4a" stroke-width="2"><path d="M14,33 V4 H34"/><path d="M14,10 L20,4"/><path d="M30,4 V14"/><path d="M2,33 H34"/><path d="M4,33 V24 H12 V33"/><path d="M20,33 V20 H30 V33"/></svg>
    Construction<br>Sites
  </div>
  <div class="sector-divider" style="left:305px"></div>
  <div class="sector" style="left:361px">
    <svg width="36" height="34" viewBox="0 0 36 34" fill="none" stroke="#131b4a" stroke-width="2"><path d="M3,33 V5 M33,33 V5"/><path d="M3,12 C12,4 24,4 33,12"/><path d="M9,33 V10 M15,33 V8 M21,33 V8 M27,33 V10"/><path d="M2,33 H34"/></svg>
    Gated<br>Communities
  </div>
  <div class="sector-divider" style="left:408px"></div>
  <div class="sector" style="left:464px">
    <svg width="36" height="34" viewBox="0 0 36 34" fill="none" stroke="#131b4a" stroke-width="2"><path d="M10,33 V3 H26 V33"/><path d="M3,33 V14 H10 M26,14 H33 V33"/><path d="M1,33 H35"/><path d="M14,8 H16 M20,8 H22 M14,14 H16 M20,14 H22 M14,20 H16 M20,20 H22 M15,33 V26 H21 V33"/></svg>
    Commercial<br>Properties
  </div>

  <div class="region" style="top:433px">
    <div class="region__small">PROUDLY SERVING</div>
    <div class="region__big">NEW JERSEY</div>
  </div>

  <svg class="cta__icon" width="47" height="47" viewBox="0 0 47 47" fill="none" stroke="#fff" stroke-width="2.5" aria-hidden="true">
    <circle cx="23.5" cy="23.5" r="21.5"/>
    <path d="M16,12 L20,12 L22,18 L19,21 C20.5,24.5 22.5,26.5 26,28 L29,25 L35,27 L35,31 C35,33 33,35 31,35 C21,34 13,26 12,16 C12,14 14,12 16,12 Z" stroke-linejoin="round"/>
  </svg>
  <div class="cta">
    <div class="cta__top">CALL TODAY FOR A</div>
    <div><span class="cta__free">FREE</span><span class="cta__rest">SECURITY ASSESSMENT</span></div>
  </div>

  <div class="contact" style="left:401px;top:483px">
    <div class="contact__row">
      <svg width="16" height="16" viewBox="0 0 16 16" fill="none" stroke="#fff" stroke-width="1.2"><circle cx="8" cy="8" r="7"/><path d="M5.5,4 L7,4 L7.5,6 L6.5,7 C7,8.3 7.7,9 9,9.5 L10,8.5 L12,9 L12,10.5 C12,11.3 11.3,12 10.5,12 C7,11.7 4.3,9 4,5.5 C4,4.7 4.7,4 5.5,4 Z"/></svg>
      <span>555-014-2277</span>
    </div>
    <div class="contact__row">
      <svg width="16" height="16" viewBox="0 0 16 16" fill="none" stroke="#fff" stroke-width="1.2"><circle cx="8" cy="8" r="7"/><ellipse cx="8" cy="8" rx="3" ry="7"/><path d="M1,8 H15 M2.5,4.5 H13.5 M2.5,11.5 H13.5"/></svg>
      <span>www.<span class="hl">vantersecurity</span>.com</span>
    </div>
  </div>
</section>

<!-- BACK -->
<section class="card card--back">
  <svg class="layer" viewBox="0 0 801 534" aria-hidden="true">
    <defs>
      <linearGradient id="ctaBlue2" x1="0" x2="1"><stop offset="0" stop-color="#1b8fd1"/><stop offset="1" stop-color="#156fae"/></linearGradient>
    </defs>
    <path d="M0,0 H462 C472,160 440,330 350,470 L340,534 H0 Z" fill="#131b4a"/>
    <path d="M486,0 C494,170 460,340 360,480" fill="none" stroke="#1b8fd1" stroke-width="5"/>
    <path d="M363,472 H597 L612,534 H385 Z" fill="#131b4a"/>
    <path d="M0,459 H352 Q362,459 366,468 L385,534 H0 Z" fill="url(#ctaBlue2)"/>
  </svg>

  <div class="headline" style="left:26px;top:35px;font-size:62px;transform:scaleX(1.28)">PROTECT</div>
  <div class="subhead" style="left:24px;top:92px;font-size:28px;letter-spacing:2.6px;color:var(--white)">BUSINESS WITH CONFIDENCE</div>
  <div class="rule" style="left:28px;top:128px;width:390px"></div>

  <div class="section-title" style="top:142px">WHY CHOOSE US?</div>
  <div class="reason" style="left:40px;top:171px">
    <svg width="26" height="28" viewBox="0 0 26 28" fill="none" stroke="#fff" stroke-width="1.6"><path d="M13,2 C18,4 22,4 24,4 C24,16 20,23 13,26 C6,23 2,16 2,4 C4,4 8,4 13,2 Z"/><path d="M8,14 L12,18 L18,10"/></svg>
    <span>Retired Law<br>Enforcement Leadership</span>
  </div>
  <div class="reason-divider" style="left:273px;top:174px"></div>
  <div class="reason" style="left:248px;top:171px">
    <span style="width:26px"></span>
    <svg width="26" height="28" viewBox="0 0 26 28" fill="none" stroke="#fff" stroke-width="1.6"><rect x="3" y="3" width="18" height="23" rx="2"/><path d="M8,3 V1 H16 V3"/><path d="M7,11 H17 M7,16 H17 M7,21 H13"/></svg>
    <span>Customized<br>Security Plans</span>
  </div>
  <div class="reason" style="left:40px;top:216px">
    <svg width="26" height="28" viewBox="0 0 26 28" fill="none" stroke="#fff" stroke-width="1.6"><circle cx="13" cy="14" r="11"/><path d="M13,7 V14 L18,17"/></svg>
    <span>Fast &amp;<br>Reliable Response</span>
  </div>
  <div class="reason-divider" style="left:272px;top:219px"></div>
  <div class="reason" style="left:248px;top:216px">
    <span style="width:26px"></span>
    <svg width="26" height="28" viewBox="0 0 26 28" fill="none" stroke="#fff" stroke-width="1.6"><circle cx="13" cy="14" r="11"/><path d="M8,14 L12,18 L18,10"/></svg>
    <span>Licensed &amp;<br>Professional Guards</span>
  </div>

  <div class="section-title" style="top:264px">OUR SERVICES</div>

  <div class="service" style="left:40px;top:293px"><svg width="30" height="32" viewBox="0 0 30 32"><path d="M15,2 C21,5 26,5 28,5 C28,19 23,27 15,30 C7,27 2,19 2,5 C4,5 9,5 15,2 Z" fill="#fff" stroke="#1b8fd1" stroke-width="2"/><path d="M9,16 L13,20 L21,11" fill="none" stroke="#131b4a" stroke-width="2.2"/></svg><span>Armed &amp; Unarmed<br>Security Guards</span></div>
  <div class="service" style="left:199px;top:293px"><svg width="30" height="32" viewBox="0 0 30 32"><path d="M15,2 C21,5 26,5 28,5 C28,19 23,27 15,30 C7,27 2,19 2,5 C4,5 9,5 15,2 Z" fill="#fff" stroke="#1b8fd1" stroke-width="2"/><path d="M9,16 L13,20 L21,11" fill="none" stroke="#131b4a" stroke-width="2.2"/></svg><span style="margin-left:6px">Permanent &amp;<br>Emergency Coverage</span></div>

  <div class="service" style="left:40px;top:343px"><svg width="30" height="32" viewBox="0 0 30 32"><path d="M15,2 C21,5 26,5 28,5 C28,19 23,27 15,30 C7,27 2,19 2,5 C4,5 9,5 15,2 Z" fill="#fff" stroke="#1b8fd1" stroke-width="2"/><path d="M9,16 L13,20 L21,11" fill="none" stroke="#131b4a" stroke-width="2.2"/></svg><span>Mobile<br>Patrols</span></div>
  <div class="service" style="left:135px;top:343px"><svg width="30" height="32" viewBox="0 0 30 32"><path d="M15,2 C21,5 26,5 28,5 C28,19 23,27 15,30 C7,27 2,19 2,5 C4,5 9,5 15,2 Z" fill="#fff" stroke="#1b8fd1" stroke-width="2"/><path d="M9,16 L13,20 L21,11" fill="none" stroke="#131b4a" stroke-width="2.2"/></svg><span>Property<br>Checks</span></div>
  <div class="service" style="left:265px;top:341px"><svg width="30" height="32" viewBox="0 0 30 32"><path d="M15,2 C21,5 26,5 28,5 C28,19 23,27 15,30 C7,27 2,19 2,5 C4,5 9,5 15,2 Z" fill="#fff" stroke="#1b8fd1" stroke-width="2"/><path d="M9,16 L13,20 L21,11" fill="none" stroke="#131b4a" stroke-width="2.2"/></svg><span>ALPR Camera<br>Systems</span></div>

  <div class="service" style="left:40px;top:396px"><svg width="30" height="32" viewBox="0 0 30 32"><path d="M15,2 C21,5 26,5 28,5 C28,19 23,27 15,30 C7,27 2,19 2,5 C4,5 9,5 15,2 Z" fill="#fff" stroke="#1b8fd1" stroke-width="2"/><path d="M9,16 L13,20 L21,11" fill="none" stroke="#131b4a" stroke-width="2.2"/></svg><span>Alarm<br>Response</span></div>
  <div class="service" style="left:135px;top:396px"><svg width="30" height="32" viewBox="0 0 30 32"><path d="M15,2 C21,5 26,5 28,5 C28,19 23,27 15,30 C7,27 2,19 2,5 C4,5 9,5 15,2 Z" fill="#fff" stroke="#1b8fd1" stroke-width="2"/><path d="M9,16 L13,20 L21,11" fill="none" stroke="#131b4a" stroke-width="2.2"/></svg><span>Mobile Security<br>Cameras</span></div>
  <div class="service" style="left:265px;top:397px"><svg width="30" height="32" viewBox="0 0 30 32"><path d="M15,2 C21,5 26,5 28,5 C28,19 23,27 15,30 C7,27 2,19 2,5 C4,5 9,5 15,2 Z" fill="#fff" stroke="#1b8fd1" stroke-width="2"/><path d="M9,16 L13,20 L21,11" fill="none" stroke="#131b4a" stroke-width="2.2"/></svg><span>Fire Watch<br>Services</span></div>

  <div class="stamp"></div>
  <div class="address-line" style="left:491px;top:170px;width:282px"></div>
  <div class="address-line" style="left:491px;top:211px;width:282px"></div>
  <div class="address-line" style="left:482px;top:260px;width:291px"></div>
  <div class="address-line" style="left:465px;top:309px;width:308px"></div>
  <div class="address-line" style="left:447px;top:359px;width:326px"></div>
  <div class="address-line" style="left:410px;top:413px;width:363px"></div>

  <svg class="cta__icon" width="47" height="47" viewBox="0 0 47 47" fill="none" stroke="#fff" stroke-width="2.5" aria-hidden="true">
    <circle cx="23.5" cy="23.5" r="21.5"/>
    <path d="M16,12 L20,12 L22,18 L19,21 C20.5,24.5 22.5,26.5 26,28 L29,25 L35,27 L35,31 C35,33 33,35 31,35 C21,34 13,26 12,16 C12,14 14,12 16,12 Z" stroke-linejoin="round"/>
  </svg>
  <div class="cta">
    <div class="cta__top">CALL TODAY FOR A</div>
    <div><span class="cta__free">FREE</span><span class="cta__rest">SECURITY ASSESSMENT</span></div>
  </div>

  <div class="contact" style="left:392px;top:483px;font-size:16.5px">
    <div class="contact__row" style="gap:8px">
      <svg width="14" height="14" viewBox="0 0 16 16" fill="none" stroke="#fff" stroke-width="1.2"><circle cx="8" cy="8" r="7"/><path d="M5.5,4 L7,4 L7.5,6 L6.5,7 C7,8.3 7.7,9 9,9.5 L10,8.5 L12,9 L12,10.5 C12,11.3 11.3,12 10.5,12 C7,11.7 4.3,9 4,5.5 C4,4.7 4.7,4 5.5,4 Z"/></svg>
      <span>555-014-2277</span>
    </div>
    <div class="contact__row" style="gap:8px">
      <svg width="14" height="14" viewBox="0 0 16 16" fill="none" stroke="#fff" stroke-width="1.2"><circle cx="8" cy="8" r="7"/><ellipse cx="8" cy="8" rx="3" ry="7"/><path d="M1,8 H15 M2.5,4.5 H13.5 M2.5,11.5 H13.5"/></svg>
      <span>www.<span class="hl">vantersecurity</span>.com</span>
    </div>
  </div>

  <div class="brand" style="left:620px;top:480px;gap:6px">
    <span class="brand__mark" style="width:24px;height:24px"></span>
    <span class="brand__name" style="font-size:30px">VANTER</span>
  </div>
  <div class="brand__sub" style="left:645px;top:512px;font-size:8.5px;letter-spacing:1.3px">SECURITY &amp; INVESTIGATIONS</div>
</section>

</body>
</html>
```